Welding Fabrication and Inspection Business Card Design

Welding Fabrication and Inspection Services,

Business

Industrial Machinery ServicesMohammed Rahim30 Ballarat Street, Mount Gravatt East.4122.QLD

```html
<!DOCTYPE html>
<html lang="en">
<head>
<meta charset="utf-8">
<title>Tarnwell Forge Services – Business Card</title>
<link rel="stylesheet" href="https://fonts.googleapis.com/css2?family=Barlow:wght@600&family=Open+Sans:wght@400;600&display=swap">
<style>
  :root {
    --page-bg: #e9e6e2;
    --card-top: #f4f3f1;
    --card-bottom: #e4e1de;
    --ink: #1c1c1c;
    --ink-soft: #3a3a3a;
    --band: #2a2625;
    --band-edge: #161313;
    --band-text: #d9d2cf;
    --rule: #1e1e1e;
  }
  * { margin: 0; padding: 0; box-sizing: border-box; }
  html, body {
    width: 1200px; height: 970px; overflow: hidden;
    background: var(--page-bg);
  }
  .canvas { position: relative; width: 1200px; height: 970px; }
  .card {
    position: absolute; left: 100px; top: 201px;
    width: 1000px; height: 568px;
    background: linear-gradient(180deg, var(--card-top), var(--card-bottom));
    box-shadow: 0 10px 30px rgba(0,0,0,.18);
    overflow: hidden;
  }
  .brand {
    position: absolute; left: 82px; top: 280px;
    display: flex; align-items: center; gap: 12px;
    font-family: "Barlow", sans-serif; font-weight: 600;
    font-size: 26px; color: var(--ink-soft);
  }
  .brand-square { width: 16px; height: 16px; background: var(--ink-soft); }
  .divider {
    position: absolute; left: 500px; top: 118px;
    width: 2px; height: 295px; background: var(--rule);
  }
  .holder-name {
    position: absolute; left: 541px; top: 148px;
    font-family: "Open Sans", sans-serif; font-weight: 600;
    font-size: 33px; color: var(--ink);
  }
  .contacts {
    position: absolute; left: 545px; top: 276px;
    list-style: none;
    font-family: "Open Sans", sans-serif; font-weight: 600;
    font-size: 28px; color: var(--ink);
  }
  .contacts li { display: flex; align-items: center; gap: 12px; height: 35px; }
  .contacts svg { width: 30px; height: 30px; flex: none; }
  .address-band {
    position: absolute; left: 0; bottom: 0; width: 100%; height: 70px;
    background: linear-gradient(180deg, var(--band-edge), var(--band) 40%, #3b3534);
    border-top: 3px solid var(--card-bottom);
    outline: 3px solid var(--band-edge);
    display: flex; align-items: center; justify-content: center;
    font-family: "Open Sans", sans-serif; font-weight: 400;
    font-size: 27px; color: var(--band-text);
  }
</style>
</head>
<body>
<div class="canvas">
  <section class="card">
    <div class="brand"><span class="brand-square"></span>Tarnwell Forge Services</div>
    <div class="divider"></div>
    <h1 class="holder-name">Khalid Nasser</h1>
    <ul class="contacts">
      <li>
        <svg viewBox="0 0 30 30" aria-label="Phone"><rect width="30" height="30" fill="#1c1c1c"/><path d="M7 12c0-3 4-5 8-5s8 2 8 5l-3 1-1-2c-2-1-6-1-8 0l-1 2zM9 15h12l2 8H7z" fill="#fff"/></svg>
        000-000-0000
      </li>
      <li>
        <svg viewBox="0 0 30 30" aria-label="Fax"><rect width="30" height="30" fill="#1c1c1c"/><path d="M10 6h10v5H10zM6 12h18v9H6zM10 18h10v6H10z" fill="#fff"/><rect x="11" y="19" width="8" height="1.5" fill="#1c1c1c"/></svg>
        000-000-0000
      </li>
      <li>
        <svg viewBox="0 0 30 30" aria-label="Email"><rect width="30" height="30" fill="#1c1c1c"/><rect x="6" y="9" width="18" height="12" fill="#fff"/><path d="M6 9l9 7 9-7" fill="none" stroke="#1c1c1c" stroke-width="1.5"/></svg>
        office@tarnwellforge.com
      </li>
    </ul>
    <footer class="address-band">17 Corrowen Street, Brindle Vale East. 4178.QLD</footer>
  </section>
</div>
</body>
</html>
```